Quillo Mobile Phone colors and content

Looking to have an impact both on messaging and colors for my mobile website
www.maplegrovefin.loan
also, i have upload my first draft of the mobile site, including messaging. that is open to the designer. In the end, i want the mobile phone messaging to resonate for someone who wants to build their credit.
Dont worry about the color combination on the document.

Target Market(s)

Finance - those with super poor credit.

Industry/Entity Type

Finance - credit building

Number of Pages Required

5+ page

Font styles to use
Other font styles liked:
• Inter

Requirements
Must have
• flow and impact
Nice to have
• look at the documents uploaded
Should not have
• not have dark background colors. background should be white.

```html
<!DOCTYPE html>
<html lang="en">
<head>
<meta charset="utf-8">
<title>Quillo – Credit Builder Loans mobile screens</title>
<link rel="stylesheet" href="https://fonts.googleapis.com/css2?family=Inter:wght@400;500;600;700;800&display=swap">
<style>
  :root {
    --navy: #03284f;
    --white: #ffffff;
    --ink: #111418;
    --body-grey: #5c6168;
    --brand-blue: #0b4f94;
    --brand-green: #0fa846;
    --dot-grey: #b9bec6;
    --illustration-top: #f3d9bf;
    --illustration-bottom: #dfe8f3;
  }
  * { box-sizing: border-box; margin: 0; padding: 0; }
  html, body { width: 1200px; height: 2994px; overflow: hidden; }
  body {
    background: var(--navy);
    font-family: "Inter", Arial, sans-serif;
    color: var(--ink);
    position: relative;
  }

  .poster-header {
    position: absolute; top: 112px; left: 0; width: 1200px;
    text-align: center;
  }
  .poster-header .brand-name {
    font-size: 72px; font-weight: 800; color: var(--white);
    letter-spacing: 0.5px; line-height: 1;
  }
  .poster-header .brand-tagline {
    margin-top: 26px; font-size: 38px; font-weight: 700;
    color: var(--brand-green); line-height: 1;
  }

  .screen {
    position: absolute; width: 333px; height: 782px;
    background: var(--white); border-radius: 44px;
  }
  .screen > * { position: absolute; left: 0; width: 100%; text-align: center; }

  .screen-brand { top: 62px; }
  .screen-brand .brand-name {
    font-size: 22px; font-weight: 800; color: var(--ink); line-height: 1;
  }
  .screen-brand .brand-tagline {
    margin-top: 6px; font-size: 12px; font-weight: 700;
    color: var(--brand-green); letter-spacing: 0.2px;
  }

  .mascot {
    left: 98px; width: 137px; height: 160px; border-radius: 20px;
    background: linear-gradient(180deg, var(--illustration-top), var(--illustration-bottom));
  }
  .mascot-name {
    font-size: 19px; font-weight: 500; color: var(--brand-blue);
    letter-spacing: 1.5px;
  }

  .step-label {
    font-size: 10px; font-weight: 700; color: var(--brand-blue);
  }
  .step-title {
    left: 20px; width: 293px;
    font-size: 21px; font-weight: 400; line-height: 23px; color: var(--ink);
  }
  .step-rule {
    left: 149px; width: 35px; height: 2px; background: var(--brand-blue);
  }
  .step-body {
    left: 40px; width: 253px;
    font-size: 9.5px; line-height: 13px; color: var(--body-grey);
  }
  .step-body p + p { margin-top: 7px; }

  .pager {
    display: flex; justify-content: center; align-items: center; gap: 3px;
    height: 5px;
  }
  .pager span { width: 5px; height: 5px; border-radius: 50%; background: var(--dot-grey); }
  .pager span.is-active { width: 27px; border-radius: 3px; background: var(--brand-blue); }

  .apply-button {
    left: 50px; width: 233px; height: 32px; border-radius: 16px;
    background: var(--brand-blue); color: var(--white);
    font-size: 10px; font-weight: 700; line-height: 32px;
    text-decoration: none;
  }
</style>
</head>
<body>

<header class="poster-header">
  <div class="brand-name">Quillo</div>
  <div class="brand-tagline">Credit Builder Loans</div>
</header>

<!-- Step 1 -->
<section class="screen" style="left:212px; top:360px;">
  <div class="screen-brand"><div class="brand-name">Quillo</div><div class="brand-tagline">Credit Builder Loans</div></div>
  <div class="step-label" style="top:295px;">Step 1</div>
  <h2 class="step-title" style="top:315px;">A Better Way to Rebuild<br>Credit 3 Bold Steps</h2>
  <div class="step-rule" style="top:371px;"></div>
  <div class="step-body" style="top:384px;"><p>We'll help you do it effectively—with real tools, real progress, and real incentives.</p></div>
  <a class="apply-button" style="top:463px;" href="#">Apply Now</a>
</section>

<!-- Step 2 -->
<section class="screen" style="left:642px; top:360px;">
  <div class="screen-brand"><div class="brand-name">Quillo</div><div class="brand-tagline">Credit Builder Loans</div></div>
  <div class="mascot" style="top:137px;" role="img" aria-label="Illustration of the Dr. Quillo mascot, a friendly doctor in a white coat with a stethoscope and credit-score badge"></div>
  <div class="mascot-name" style="top:305px;">Dr. Quillo</div>
  <div class="step-label" style="top:357px;">Step 2</div>
  <h2 class="step-title" style="top:377px;">A $2,000 Credit Builder<br>Loan</h2>
  <div class="step-rule" style="top:434px;"></div>
  <div class="step-body" style="top:446px;">
    <p>Make on-time payments on a $2,000 Credit Builder Loan designed to help establish real credit history.</p>
    <p>As you progress, you unlock a Northpay credit card option.</p>
  </div>
  <div class="pager" style="top:536px;"><span></span><span class="is-active"></span><span></span><span></span></div>
  <a class="apply-button" style="top:616px;" href="#">Apply Now</a>
</section>

<!-- Step 3 -->
<section class="screen" style="left:204px; top:1229px;">
  <div class="screen-brand"><div class="brand-name">Quillo</div><div class="brand-tagline">Credit Builder Loans</div></div>
  <div class="step-label" style="top:246px;">Step 3</div>
  <h2 class="step-title" style="top:265px;">We Put Our Money Where<br>Our Mouth Is</h2>
  <div class="step-rule" style="top:324px;"></div>
  <div class="step-body" style="top:337px;">
    <p>Upon reaching Platinum Quillo Status, eligible members may receive a matching contribution of up to $150 toward an approved secured credit card.</p>
    <p>A strong on-time payment history with us is required.</p>
    <p>Your responsible progress unlocks real value—not gimmicks.</p>
  </div>
  <div class="pager" style="top:443px;"><span></span><span class="is-active"></span><span></span><span></span></div>
  <a class="apply-button" style="top:512px;" href="#">Apply Now</a>
</section>

<!-- Step 4 -->
<section class="screen" style="left:643px; top:1221px;">
  <div class="screen-brand"><div class="brand-name">Quillo</div><div class="brand-tagline">Credit Builder Loans</div></div>
  <div class="step-label" style="top:257px;">Step 4</div>
  <h2 class="step-title" style="top:275px;">Graduate to a larger<br>Credit line with an Unsecured<br>Northpay Creditcard</h2>
  <div class="step-rule" style="top:356px;"></div>
  <div class="step-body" style="top:368px;">
    <p>Continued responsible use may qualify you for a higher-credit-limit unsecured credit card.</p>
    <p>No security deposit would be required.</p>
  </div>
  <div class="pager" style="top:431px;"><span></span><span class="is-active"></span><span></span><span></span></div>
  <a class="apply-button" style="top:502px;" href="#">Apply Now</a>
</section>

<!-- Step 5 -->
<section class="screen" style="left:204px; top:2090px;">
  <div class="screen-brand"><div class="brand-name">Quillo</div><div class="brand-tagline">Credit Builder Loans</div></div>
  <div class="step-label" style="top:270px;">Step 5</div>
  <h2 class="step-title" style="top:290px;">Ongoing Credit Wellness</h2>
  <div class="step-rule" style="top:323px;"></div>
  <div class="step-body" style="top:336px;">
    <p>Track your progress, monitor your credit, and get guidance along the way.</p>
    <p>Dr. Quillo helps you understand what matters—and provides concrete strategies to improve your credit.</p>
  </div>
  <a class="apply-button" style="top:488px;" href="#">Apply Now</a>
</section>

</body>
</html>
```